Events & Entertainment Production Coordination Business Cards

We need a business card for a new company based in Los Angeles called "Bright Stage Works"
Our company brings people together for events and helps coordinate different productions. We bring artists from a different country to perform or do events in the U.S.
We are looking for something fun, lively, colorful, creative, and simple.
Nothing that looks too crisp, dark, stiff, or modern.
We connect people from different parts of the world, so definitely something eye-catching will be great!
Colors we would like to see are Black, Yellow, Red, White, Brown to name a few. (Feel free to use more!)
(Double-sided is an option also)
Industry/Entity Type
Business
Contact Information for Business Card
Contact Information to put on Business Card:
Name
Title
Address - 2 lines
Phone - place for 3 numbers
E-mail
URL
Look and feel

```html
<!DOCTYPE html>
<html lang="en">
<head>
<meta charset="utf-8">
<title>Bright Stage Works — Business Cards</title>
<link rel="stylesheet" href="https://fonts.googleapis.com/css2?family=Arimo:wght@700&family=Open+Sans:wght@400;600;700&display=swap">
<style>
  :root {
    --stage: #2b2b2d;
    --card-white: #ffffff;
    --card-black: #0b0b0b;
    --brand-orange: #ec5a24;
    --sun-yellow: #f7c21a;
    --text-light: #f2f2f2;
    --text-muted: #d9d9d9;
  }
  * { box-sizing: border-box; margin: 0; padding: 0; }
  html, body {
    width: 1200px; height: 900px; overflow: hidden;
    background: var(--stage);
  }
  .canvas {
    position: relative; width: 1200px; height: 900px;
  }
  .card {
    position: absolute; left: 340px;
    width: 520px; height: 300px;
    border-radius: 22px; overflow: hidden;
    background: var(--card-white);
    box-shadow: 0 10px 24px rgba(0,0,0,.45);
  }
  .card--front { top: 110px; }
  .card--back { top: 470px; }

  .brand {
    display: flex; align-items: center; gap: 12px;
    font-family: "Arimo", Arial, sans-serif; font-weight: 700;
    color: var(--brand-orange);
  }
  .brand__dot {
    border-radius: 50%; background: var(--sun-yellow);
    border: 4px solid var(--brand-orange); flex: none;
  }
  .card--front .brand {
    position: absolute; left: 100px; top: 122px;
    font-size: 34px;
  }
  .card--front .brand__dot { width: 54px; height: 54px; }

  /* back side */
  .back__top {
    position: absolute; left: 0; top: 0; width: 100%; height: 150px;
    background: var(--card-white);
  }
  .back__bottom {
    position: absolute; left: 0; top: 150px; width: 100%; height: 150px;
    background: var(--card-black);
    border-top: 3px solid var(--brand-orange);
  }
  .back__name {
    position: absolute; left: 34px; top: 100px;
    font-family: "Arimo", Arial, sans-serif; font-weight: 700;
    font-size: 28px; color: var(--brand-orange);
  }
  .back__emblem {
    position: absolute; left: 328px; top: 92px;
    width: 112px; height: 112px; border-radius: 50%;
    background: var(--sun-yellow);
    border: 5px solid var(--brand-orange);
  }
  .person {
    position: absolute; right: 258px; top: 200px;
    text-align: right; font-family: "Open Sans", Arial, sans-serif;
    color: var(--text-light);
  }
  .person__name {
    font-weight: 700; font-size: 19px; color: var(--brand-orange);
    letter-spacing: .5px; line-height: 1.1;
  }
  .person__title { font-size: 11px; letter-spacing: 1px; margin-bottom: 4px; }
  .person__address { font-size: 12px; line-height: 1.35; }
  .divider {
    position: absolute; left: 276px; top: 204px; width: 1px; height: 78px;
    background: #555;
  }
  .contacts {
    position: absolute; left: 290px; top: 206px; list-style: none;
    font-family: "Open Sans", Arial, sans-serif; font-size: 12px;
    color: var(--text-light); line-height: 15px;
  }
  .contacts li { display: flex; align-items: center; gap: 7px; }
  .contacts svg { width: 10px; height: 10px; flex: none; }
</style>
</head>
<body>
<main class="canvas">
  <section class="card card--front" aria-label="Card front">
    <div class="brand"><span class="brand__dot"></span>Bright Stage Works</div>
  </section>

  <section class="card card--back" aria-label="Card back">
    <div class="back__top"></div>
    <div class="back__bottom"></div>
    <div class="back__name">Bright Stage Works</div>
    <div class="back__emblem"></div>

    <div class="person">
      <p class="person__name">DANA WHITFIELD</p>
      <p class="person__title">DIRECTOR</p>
      <p class="person__address">14 - 20 Harbor Lane St<br>Westmere Valley 2210 Australia</p>
    </div>
    <div class="divider"></div>
    <ul class="contacts">
      <li><svg viewBox="0 0 10 10"><path d="M2 1 L4 1 L4.6 3 L3.4 4 Q4.5 6 6 6.6 L7 5.4 L9 6 L9 8 Q5 9 1.5 5 Q1 3 2 1Z" fill="var(--brand-orange)"/></svg>+310 5550-1842</li>
      <li><svg viewBox="0 0 10 10"><rect x="2.5" y="0.5" width="5" height="9" rx="1" fill="none" stroke="var(--brand-orange)" stroke-width="1.2"/></svg>+310 5550-2976</li>
      <li><svg viewBox="0 0 10 10"><rect x="1" y="4" width="8" height="5" rx="1" fill="var(--brand-orange)"/><rect x="3" y="1" width="4" height="3" fill="var(--brand-orange)"/></svg>+310 5550-3718</li>
      <li><svg viewBox="0 0 10 10"><rect x="0.8" y="2" width="8.4" height="6" fill="none" stroke="var(--brand-orange)" stroke-width="1.1"/><path d="M1 2.3 L5 5.5 L9 2.3" fill="none" stroke="var(--brand-orange)" stroke-width="1.1"/></svg>info@brightstageworks.com</li>
      <li><svg viewBox="0 0 10 10"><circle cx="5" cy="5" r="4.2" fill="none" stroke="var(--brand-orange)" stroke-width="1.1"/><path d="M0.8 5 H9.2 M5 0.8 V9.2" stroke="var(--brand-orange)" stroke-width="0.9"/></svg>www.brightstageworks.com</li>
    </ul>
  </section>
</main>
</body>
</html>
```